Marrowby's Vacation Rentals Business Card

Multi Million dollar villa rentals in the Dominican Republic.

Industry/Entity Type

Business

Contact Information for Business Card

I am looking for a high-end look around my company name/logo (see attached) on one side incorporating the following info: first and last name, title, address, phone #, email and company website. On the backside I want to add a full color picture of one of our villas (see attached).

```html
<!DOCTYPE html>
<html lang="en">
<head>
<meta charset="utf-8">
<title>Marrowby's Vacation Rentals – Business Card</title>
<link rel="stylesheet" href="https://fonts.googleapis.com/css2?family=Open+Sans:wght@400;600;700&display=swap">
<style>
  :root {
    --page-bg: #e6e6e6;
    --card-white: #ffffff;
    --brand-orange: #f47a20;
    --ink-black: #1c1c1c;
    --text-dark: #2a2a2a;
    --photo-light: #c9dbe8;
    --photo-deep: #3d9fd9;
  }
  * { box-sizing: border-box; margin: 0; padding: 0; }
  html, body {
    width: 1200px; height: 969px; overflow: hidden;
    background: var(--page-bg);
    font-family: "Open Sans", Arial, sans-serif;
  }
  .sheet {
    width: 1200px; height: 969px;
    display: flex; align-items: center; justify-content: center; gap: 48px;
  }
  .card {
    position: relative;
    width: 540px; height: 308px;
    background: var(--card-white);
    overflow: hidden;
    box-shadow: 0 2px 6px rgba(0,0,0,0.15);
  }

  /* back side */
  .villa-photo {
    position: absolute; inset: 0;
    background: linear-gradient(160deg, var(--photo-light) 0%, var(--photo-deep) 100%);
  }

  /* front side */
  .edge-tab {
    position: absolute; left: 0; top: 78px;
    width: 14px; height: 22px; background: var(--brand-orange);
  }
  .holder { position: absolute; left: 30px; top: 46px; }
  .holder-name {
    color: var(--brand-orange); font-weight: 700; font-size: 18px; line-height: 1.15;
  }
  .holder-title { color: var(--text-dark); font-size: 13px; font-weight: 600; }

  .brand {
    position: absolute; left: 188px; top: 60px;
    display: flex; align-items: center; gap: 12px;
  }
  .brand-dot {
    width: 48px; height: 48px; border-radius: 50%; background: var(--brand-orange);
  }
  .brand-name {
    color: var(--ink-black); font-weight: 600; font-size: 28px; line-height: 1.1;
  }

  .address {
    position: absolute; right: 26px; top: 142px;
    text-align: right; color: var(--text-dark); font-size: 13px; line-height: 1.35;
  }
  .band-orange {
    position: absolute; right: 0; top: 186px;
    width: 218px; height: 22px; background: var(--brand-orange);
  }
  .band-black {
    position: absolute; left: 0; bottom: 14px;
    width: 322px; height: 22px; background: var(--ink-black);
  }

  .contacts {
    position: absolute; left: 30px; top: 200px;
    list-style: none; color: var(--ink-black); font-size: 15px; line-height: 1.4;
  }
  .contacts li { display: flex; align-items: center; gap: 7px; }
  .contacts svg { width: 13px; height: 13px; flex: none; }
</style>
</head>
<body>
<main class="sheet">

  <section class="card card-back">
    <div class="villa-photo" role="img" aria-label="Photograph of a white villa with arched terrace and blue pool with sun loungers"></div>
  </section>

  <section class="card card-front">
    <div class="edge-tab"></div>

    <div class="holder">
      <p class="holder-name">Julien Dufresne</p>
      <p class="holder-title">President</p>
    </div>

    <div class="brand">
      <span class="brand-dot"></span>
      <p class="brand-name">Marrowby's<br>Vacation Rentals</p>
    </div>

    <p class="address">4470 Rue des Pins<br>Laval, QC H7T2K9</p>

    <div class="band-orange"></div>

    <ul class="contacts">
      <li>
        <svg viewBox="0 0 16 16"><path fill="#f47a20" d="M3 1l3 3-2 2c1 2 3 4 5 5l2-2 3 3-2 3C6 15 1 10 0 4z"/></svg>
        8885550147
      </li>
      <li>
        <svg viewBox="0 0 16 16"><rect x="0" y="3" width="16" height="10" rx="1" fill="#f47a20"/><path d="M1 4l7 5 7-5" stroke="#fff" stroke-width="1.4" fill="none"/></svg>
        info@marrowbyvillas.com
      </li>
      <li>
        <svg viewBox="0 0 16 16"><circle cx="8" cy="8" r="8" fill="#f47a20"/><circle cx="8" cy="8" r="3" fill="#fff"/></svg>
        www.marrowbyvillas.com
      </li>
    </ul>

    <div class="band-black"></div>
  </section>

</main>
</body>
</html>
```